Dog grooming business card
This is a business card for m dog grooming business like it say above.
In the priorities box below I will have the text that I want on the card.

Industry/Entity Type

Business

Colors

Designer to choose colors to be used in the design.

Requirements
Must have
• My logo and the insurance stamp must be on the card.

Text it must have :

Professional grooming services
Email: lindomerfield@brightmail.example
Text or call 1 705 318 6052
KSR certified/member
Pet first aid certified
Next appointment ___________________________________
Nice to have
• Greens to match my logo

```html
<!DOCTYPE html>
<html lang="en">
<head>
<meta charset="utf-8">
<title>Lindo Merfield – Business Card</title>
<link rel="stylesheet" href="https://fonts.googleapis.com/css2?family=Open+Sans:wght@400;600;700&family=Bree+Serif&display=swap">
<style>
  :root {
    --lime: #8dc63f;
    --lime-soft: #a6d65a;
    --charcoal: #231f20;
    --charcoal-2: #2e2a2b;
    --paper: #fbfbf9;
    --ink: #1a1a1a;
    --badge-blue: #3a7bd5;
    --stage: #e9e9e6;
  }
  * { box-sizing: border-box; margin: 0; padding: 0; }
  html, body { width: 1200px; height: 800px; overflow: hidden; }
  body {
    background: var(--stage);
    font-family: "Open Sans", Arial, sans-serif;
    position: relative;
  }
  .card {
    position: absolute;
    top: 252px;
    width: 520px;
    height: 297px;
    overflow: hidden;
    box-shadow: 0 2px 10px rgba(0,0,0,.15);
  }
  /* Front */
  .card--front { left: 50px; background: var(--lime); }
  .front__panel {
    position: absolute;
    inset: 36px 40px;
    background: var(--charcoal);
    display: flex;
    align-items: center;
    justify-content: center;
  }
  .brand {
    display: flex;
    align-items: center;
    gap: 12px;
    font-weight: 700;
    color: var(--lime);
    white-space: nowrap;
  }
  .brand__dot { border-radius: 50%; background: var(--lime); flex: none; }
  .front__brand { font-size: 38px; }
  .front__brand .brand__dot { width: 30px; height: 30px; }

  /* Back */
  .card--back { left: 630px; background: var(--paper); }
  .back__wave { position: absolute; inset: 0; }
  .back__brand {
    position: absolute;
    left: 30px;
    top: 92px;
    font-size: 26px;
  }
  .back__brand .brand__dot { width: 22px; height: 22px; }
  .back__tagline {
    position: absolute;
    left: 30px;
    top: 136px;
    font-family: "Bree Serif", Georgia, serif;
    font-size: 16px;
    color: var(--ink);
    white-space: nowrap;
  }
  .partner-badge {
    position: absolute;
    right: 34px;
    top: 18px;
    width: 112px;
    height: 50px;
    border: 2px solid var(--badge-blue);
    border-radius: 6px;
    background: #fff;
  }
  .holder {
    position: absolute;
    right: 44px;
    top: 74px;
    text-align: right;
  }
  .holder__name { font-size: 14px; font-weight: 700; color: var(--lime); line-height: 18px; }
  .holder__role { font-size: 10px; color: var(--ink); line-height: 14px; }
  .contact {
    position: absolute;
    right: 24px;
    top: 168px;
    list-style: none;
    text-align: right;
    color: var(--lime-soft);
    font-size: 11px;
    line-height: 20px;
    white-space: nowrap;
  }
  .appointment {
    position: absolute;
    left: 30px;
    bottom: 10px;
    font-size: 10px;
    color: var(--lime-soft);
    white-space: nowrap;
  }
</style>
</head>
<body>

  <section class="card card--front" aria-label="Card front">
    <div class="front__panel">
      <div class="brand front__brand">
        <span class="brand__dot"></span>
        <span class="brand__name">Lindo Merfield</span>
      </div>
    </div>
  </section>

  <section class="card card--back" aria-label="Card back">
    <svg class="back__wave" width="520" height="297" viewBox="0 0 520 297" aria-hidden="true">
      <path d="M0,252 C180,252 250,217 310,167 C370,119 440,115 520,115 L520,297 L0,297Z" fill="var(--lime)"/>
      <path d="M0,261 C182,261 254,227 314,177 C374,129 442,124 520,124 L520,297 L0,297Z" fill="var(--charcoal-2)"/>
    </svg>

    <div class="brand back__brand">
      <span class="brand__dot"></span>
      <span class="brand__name">Lindo Merfield</span>
    </div>
    <p class="back__tagline">Professional grooming services</p>

    <div class="partner-badge" role="img" aria-label="Insurance stamp"></div>

    <div class="holder">
      <p class="holder__name">Ravi Tallen</p>
      <p class="holder__role">Manager</p>
    </div>

    <ul class="contact">
      <li>Text or call 1 705 318 6052</li>
      <li>lindomerfield@brightmail.example</li>
      <li>Pet first aid certified</li>
      <li>KSR certified/member</li>
    </ul>

    <p class="appointment">Next appointment ______________________</p>
  </section>

</body>
</html>
```